New Website for Belcourt Manor at www.belcourt.com.au

A new logo has been designed (through pixel forge) and we now want to align the look and feel of our website at www.belcourt.com.au to the new logo. The content and page names (e.g. Grounds) will remain largely unchanged for the new site, so please submit a new look "Home" page, using our new logo, current text and any photos you choose from the existing gallery at our website. I have also attached the current "Home" page photos.

Industry/Entity Type

Accommodation

Number of Pages Required

1 page

Requirements
Must have
• Logo to be presented on white background.

```html
<!DOCTYPE html>
<html lang="en">
<head>
<meta charset="utf-8">
<title>Belcourt Manor — Home</title>
<link rel="stylesheet" href="https://fonts.googleapis.com/css2?family=Didact+Gothic&family=Open+Sans:wght@400;600&family=Poppins:wght@600&display=swap">
<style>
  :root {
    --brand-blue: #075ea3;
    --accent-yellow: #fdd000;
    --ink: #1f1f1f;
    --muted: #3a3a3a;
    --rule: #9a9a9a;
    --nav-band: rgba(235, 235, 235, 0.88);
    --footer-bg: #2b2b2b;
    --footer-text: #e8e8e8;
    --panel-grey: #ececec;
    --white: #ffffff;
  }
  * { box-sizing: border-box; margin: 0; padding: 0; }
  html, body { width: 914px; height: 1200px; overflow: hidden; background: var(--white); }
  body { position: relative; font-family: "Open Sans", sans-serif; color: var(--ink); }

  .site-header { position: absolute; top: 0; left: 0; width: 914px; height: 90px; display: flex; align-items: center; justify-content: center; gap: 10px; }
  .brand-mark { width: 22px; height: 22px; border-radius: 50%; background: var(--brand-blue); }
  .brand-name { font-family: "Open Sans", sans-serif; font-weight: 600; font-size: 30px; color: var(--brand-blue); letter-spacing: 0.5px; }

  .hero { position: absolute; top: 90px; left: 0; width: 914px; height: 419px;
    background: linear-gradient(180deg, #2f6a35 0%, #4d8a3e 18%, #d95d3a 30%, #e6c45a 55%, #d9b64c 68%, #8f8a80 82%, #6f6b63 100%); }
  .main-nav { position: absolute; top: 90px; left: 0; width: 914px; height: 56px; background: var(--nav-band); display: flex; align-items: center; justify-content: center; }
  .nav-list { display: flex; list-style: none; font-size: 12.8px; color: #111; white-space: nowrap; }
  .nav-list li + li::before { content: "|"; margin: 0 5px; }
  .nav-list .current span { border-bottom: 2px solid var(--brand-blue); padding-bottom: 2px; }

  .reservation { position: absolute; top: 509px; left: 0; width: 914px; height: 141px; background: var(--brand-blue); color: var(--white); text-align: center; }
  .reservation h2 { font-family: "Didact Gothic", sans-serif; font-weight: 400; font-size: 25px; letter-spacing: 1.5px; margin-top: 22px; }
  .reservation p { font-size: 12.5px; margin-top: 9px; opacity: 0.92; }
  .booking-form { position: absolute; top: 92px; left: 100px; width: 714px; height: 28px; }
  .field { position: absolute; top: 0; height: 24px; border-bottom: 1px solid rgba(255,255,255,0.7); font-size: 9px; letter-spacing: 0.3px; text-align: left; padding: 6px 0 0 2px; }
  .field svg { position: absolute; right: 2px; top: 4px; }
  .book-btn { position: absolute; left: 645px; top: 0; width: 68px; height: 25px; background: var(--accent-yellow); color: #111; font-size: 12px; display: flex; align-items: center; justify-content: center; }

  .welcome { position: absolute; top: 680px; left: 0; width: 914px; text-align: center; font-family: "Didact Gothic", sans-serif; font-weight: 400; font-size: 26px; letter-spacing: 1.5px; color: #222; }
  .welcome strong { font-family: "Poppins", sans-serif; font-weight: 600; font-size: 23px; letter-spacing: 1.2px; }
  .welcome-rule { position: absolute; top: 722px; left: 372px; width: 156px; height: 1px; background: var(--rule); }

  .estate-photo { position: absolute; top: 751px; left: 110px; width: 356px; height: 318px;
    background: linear-gradient(160deg, #5f7d3f 0%, #d8764a 30%, #e4c86e 45%, #4fb0c7 62%, #3a6a32 80%, #27461f 100%); }

  .intro { position: absolute; top: 746px; left: 507px; width: 310px; }
  .intro h3 { font-weight: 400; font-size: 14.5px; color: #222; margin-bottom: 10px; }
  .intro p { font-size: 9.2px; line-height: 1.45; color: var(--muted); margin-bottom: 12px; }

  .amenities { position: absolute; top: 954px; left: 407px; width: 278px; height: 80px; border: 1px solid #dcdcdc; background: var(--white); padding: 4px 6px; }
  .amenities ul { list-style: none; background: var(--panel-grey); height: 70px; padding: 6px 0 0 18px; }
  .amenities li { display: flex; align-items: center; gap: 12px; font-size: 8px; color: #222; height: 19.5px; }
  .price-card { position: absolute; top: 954px; left: 704px; width: 109px; height: 80px; border: 1px solid #dcdcdc; padding: 4px 5px; }
  .price-card .inner { background: var(--panel-grey); height: 70px; text-align: center; padding-top: 7px; }
  .price-label { font-size: 7.5px; color: #333; }
  .price-value { font-size: 15px; color: #222; margin-top: 1px; }
  .price-btn { display: inline-block; margin-top: 3px; background: var(--accent-yellow); font-size: 9px; padding: 3px 8px; color: #111; }

  .site-footer { position: absolute; top: 1125px; left: 0; width: 914px; height: 75px; background: var(--footer-bg); display: flex; align-items: center; justify-content: center; }
  .site-footer .nav-list { color: var(--footer-text); }
</style>
</head>
<body>
  <header class="site-header">
    <span class="brand-mark"></span>
    <span class="brand-name">Belcourt Manor</span>
  </header>

  <div class="hero" role="img" aria-label="Aerial view of the yellow manor house with terracotta roofs, palms and gravel driveway"></div>

  <nav class="main-nav">
    <ul class="nav-list">
      <li class="current"><span>Home</span></li><li>Mansion</li><li>Bedrooms</li><li>Options</li><li>Owl and Lantern</li><li>Grounds</li><li>Location</li><li>Gallery</li><li>Contact</li><li>Availability</li><li>DIY Weddings</li>
    </ul>
  </nav>

  <section class="reservation">
    <h2>Resort Reservation</h2>
    <p>We’re in the business of exceeding expect ations. We give you exactly.</p>
    <div class="booking-form">
      <div class="field" style="left:0;width:117px">ARRIVAL
        <svg width="13" height="13" viewBox="0 0 13 13" fill="none" stroke="#fff" stroke-width="1"><rect x="0.5" y="1.5" width="12" height="11"/><path d="M0.5 4.5h12M3 0v3M10 0v3"/><path d="M3 7h1M6 7h1M9 7h1M3 10h1M6 10h1M9 10h1"/></svg>
      </div>
      <div class="field" style="left:142px;width:117px">ARRIVAL
        <svg width="13" height="13" viewBox="0 0 13 13" fill="none" stroke="#fff" stroke-width="1"><rect x="0.5" y="1.5" width="12" height="11"/><path d="M0.5 4.5h12M3 0v3M10 0v3"/><path d="M3 7h1M6 7h1M9 7h1M3 10h1M6 10h1M9 10h1"/></svg>
      </div>
      <div class="field" style="left:282px;width:96px">2 ROOM
        <svg width="10" height="7" viewBox="0 0 10 7" fill="none" stroke="#fff" stroke-width="1.2"><path d="M1 1l4 4 4-4"/></svg>
      </div>
      <div class="field" style="left:401px;width:96px">4 ADULD
        <svg width="10" height="7" viewBox="0 0 10 7" fill="none" stroke="#fff" stroke-width="1.2"><path d="M1 1l4 4 4-4"/></svg>
      </div>
      <div class="field" style="left:520px;width:96px">0 CHILD
        <svg width="10" height="7" viewBox="0 0 10 7" fill="none" stroke="#fff" stroke-width="1.2"><path d="M1 1l4 4 4-4"/></svg>
      </div>
      <div class="book-btn">BOOK</div>
    </div>
  </section>

  <h2 class="welcome">Welcome to <strong>Belcourt Manor</strong></h2>
  <div class="welcome-rule"></div>

  <div class="estate-photo" role="img" aria-label="Aerial view of the manor with resort pool, palms and gardens"></div>

  <article class="intro">
    <h3>Palatial Estate &amp; Luxury Resort</h3>
    <p>On over 2 manicured garden acres, Belcourt Manor is a unique Gold Coast estate, centrally located in the prestigious rural suburb of Larkspur. More about our Location</p>
    <p>The estate features a grand mansion, private pub (The Owl and Lantern), sparkling resort pool, tennis court and playground.</p>
    <p>Magnificent properties rarely feel so warm and welcoming – so browse away and visit our photo gallery<br>– and we look forward to having you stay as our guests.</p>
    <p>For prices, availability and guest reviews, visit Quillhaven Stays.</p>
  </article>

  <aside class="amenities">
    <ul>
      <li><svg width="14" height="10" viewBox="0 0 14 10" fill="none" stroke="#222" stroke-width="1.2"><path d="M1 3.5a9 9 0 0 1 12 0M3 5.5a6 6 0 0 1 8 0M5 7.5a3 3 0 0 1 4 0"/><circle cx="7" cy="9" r="0.8" fill="#222"/></svg>Free High Speed Wifi available</li>
      <li><svg width="14" height="10" viewBox="0 0 14 10"><path d="M2 5l1.5-4h7L12 5v4h-2V8H4v1H2z" fill="#222"/><circle cx="4.5" cy="6" r="0.9" fill="#eee"/><circle cx="9.5" cy="6" r="0.9" fill="#eee"/></svg>Free Parking is available</li>
      <li><svg width="14" height="10" viewBox="0 0 14 10" fill="none" stroke="#222" stroke-width="1.1"><path d="M1 5q1.5-1 3 0t3 0 3 0 3 0M1 8q1.5-1 3 0t3 0 3 0 3 0M4 4V1h5v3"/></svg>Swimming Pool , Tennis Courts</li>
    </ul>
  </aside>

  <aside class="price-card">
    <div class="inner">
      <div class="price-label">PER DAY</div>
      <div class="price-value">$540</div>
      <span class="price-btn">BOOK NOW</span>
    </div>
  </aside>

  <footer class="site-footer">
    <ul class="nav-list">
      <li>Home</li><li>Mansion</li><li>Bedrooms</li><li>Options</li><li>Owl and Lantern</li><li>Grounds</li><li>Location</li><li>Gallery</li><li>Contact</li><li>Availability</li><li>DIY Weddings</li>
    </ul>
  </footer>
</body>
</html>
```